Modern Web Design for Nonprofit Organization

Our client is looking to redesign their website. They want a modern look, clean and professional, that integrates their new brand guidelines.

Here is clients current site:
http://www.brontalvo.org/

They want their own unique design but here are some sites the clients likes:
https://www.pelorvane.com/en/
https://kelmoraswift.org/
https://www.dunbrook.com/
https://www.tovikstad.com/
https://www.quellmarren.org/

Attached please find the clients logos, color palette, site plan and design specs.

You will create a homepage mockup that will have the following sections in this order:
1. Thin Alert Bar at very top with one line message
2. Nav Bar with Logo and Main Nav (red in site plan)
3. Hero Image or Video
4. Signup Bar with name email and zip and connect button
5. Intro section with image, welcome message, and supporter counter
6. Featured Action section with call to action
7. Event section with two upcoming event cards
8. Latest News section with three latest blog post
9. Support our work (donation) section
10. Worker and Member Stories Section with feed of social posts
11. Footer.

You can use text and images from clients existing site or placeholder images and placeholder text.

Please submit as many home page mockups/idea boards as you like. Client will pick the top three and ask for some revisions. If you are selected this will lead to a lot of work for this client.

Project is private please adhere to PlanoHarbor terms of use and do not share any materials please.

QUICKEST RESPONSE PLEASE!

Thanks for looking!

Non profit donors and farmworker advocates

2 page

Sans Serif

• Adhere to brief and client brand ID
• World class design

```html
<!DOCTYPE html>
<html lang="en">
<head>
<meta charset="utf-8">
<title>AGW Foundation – Home</title>
<link href="https://fonts.googleapis.com/css2?family=Rubik:wght@400;500;700&family=Montserrat:wght@400;500;600&display=swap" rel="stylesheet">
<style>
:root{
  --red:#e30613;
  --teal:#0a979d;
  --dark:#2a2728;
  --ink:#1d1d1d;
  --text:#444;
  --alert:#fbeab8;
  --field:#eeeeee;
  --white:#fff;
}
*{box-sizing:border-box;margin:0;padding:0}
html,body{width:1200px;height:3963px;overflow:hidden}
body{position:relative;font-family:'Montserrat',sans-serif;color:var(--text);background:var(--white)}
.abs{position:absolute}
.head{font-family:'Rubik',sans-serif;font-weight:700;color:var(--ink)}
.alert-bar{left:0;top:0;width:1200px;height:42px;background:var(--alert);font-size:11px;color:#6a5c3a;text-align:center;line-height:42px;font-family:'Georgia',serif}
.brand{display:flex;align-items:center;gap:12px}
.brand .dot{width:84px;height:84px;border-radius:50%;background:var(--red)}
.brand span{font-family:'Rubik',sans-serif;font-weight:700;font-size:28px;line-height:28px;color:var(--ink)}
.util{top:75px;font-family:'Rubik',sans-serif;font-size:16px;font-weight:500;color:var(--ink);display:flex;align-items:center;gap:6px}
.donate-btn{left:897px;top:63px;width:169px;height:49px;border-radius:25px;background:var(--teal);color:#fff;font-family:'Rubik',sans-serif;font-weight:500;font-size:17px;text-align:center;line-height:49px}
.main-nav{left:0;top:137px;width:1200px;height:47px;background:var(--red)}
.main-nav a{position:absolute;top:0;line-height:47px;color:#fff;font-family:'Rubik',sans-serif;font-weight:500;font-size:18px;text-decoration:none;letter-spacing:-.3px}
.hero{left:0;top:184px;width:1200px;height:594px;background:linear-gradient(180deg,#5ea4d6 0%,#a9d2ea 30%,#c9cf7a 45%,#8fae2f 65%,#6d8a1f 100%)}
.hero-welcome{left:132px;top:355px;font-family:'Rubik',sans-serif;font-size:27px;color:var(--ink)}
.hero-title{left:132px;top:403px;font-size:50px;line-height:58px;width:460px}
.watch{left:132px;top:537px;display:flex;align-items:center;gap:16px;font-family:'Rubik',sans-serif;font-weight:700;font-size:16px;color:var(--ink)}
.watch .play{width:58px;height:58px;border-radius:50%;background:var(--red);display:flex;align-items:center;justify-content:center}
.signup{left:692px;top:262px;width:376px;height:412px;background:#fff}
.signup h3{position:absolute;left:53px;top:66px;font-family:'Rubik',sans-serif;font-weight:500;font-size:22px;color:var(--ink)}
.field{position:absolute;left:53px;width:271px;height:40px;border-radius:20px;background:var(--field);font-size:14px;color:#888;line-height:40px;padding-left:25px}
.join{position:absolute;left:53px;top:296px;width:271px;height:41px;border-radius:21px;background:var(--red);color:#fff;text-align:center;line-height:41px;font-size:15px;font-weight:500}
.section-title{width:1200px;left:0;text-align:center;font-size:38px}
.outline-btn{border:2px solid var(--teal);border-radius:30px;color:var(--ink);font-family:'Rubik',sans-serif;font-weight:500;text-align:center}
.about-title{left:131px;top:872px;font-size:43px;line-height:50px}
.body-copy{font-size:17.5px;line-height:25px;color:#333}
.photo{background:linear-gradient(135deg,#6d8a4a,#3d5a2a 55%,#a9b38a)}
.frame-a{border:4px solid var(--teal);border-radius:6px}
.frame-b{border:4px solid #cfd8d8;border-radius:6px}
.events{left:0;top:1339px;width:1200px;height:629px;background:var(--teal)}
.event-card{position:absolute;top:136px;width:396px;height:416px;background:#fff}
.event-card .img{height:211px}
.event-card h4{position:absolute;left:24px;top:234px;width:350px;font-family:'Rubik',sans-serif;font-weight:500;font-size:18px;line-height:24px;color:var(--ink)}
.event-card p{position:absolute;left:24px;top:295px;width:350px;font-size:15px;line-height:23px;color:#444}
.event-meta{position:absolute;top:377px;font-size:14.5px;font-style:italic;display:flex;gap:8px;align-items:center}
.arrow{position:absolute;top:331px;width:40px;height:40px;border-radius:50%;border:2px solid #fff;background:rgba(255,255,255,.25);display:flex;align-items:center;justify-content:center}
.news-card{position:absolute;top:2108px;width:294px;height:381px;background:#fff;box-shadow:0 2px 8px rgba(0,0,0,.12)}
.news-card .img{height:172px}
.news-card h5{position:absolute;left:17px;top:193px;width:270px;font-family:'Rubik',sans-serif;font-weight:500;font-size:16px;line-height:23px;color:var(--teal)}
.news-card p{position:absolute;left:17px;top:246px;width:270px;font-size:13.5px;line-height:19.5px;color:#444}
.news-card .outline-btn{position:absolute;left:17px;top:318px;width:124px;height:33px;line-height:29px;font-size:12.5px}
.date-badge{position:absolute;left:-8px;top:15px;width:96px;height:39px;background:var(--red);color:#fff;display:flex;align-items:center;gap:8px;padding-left:12px}
.date-badge small{font-family:'Rubik',sans-serif;font-weight:500;font-size:11px;line-height:11px}
.date-badge b{font-family:'Rubik',sans-serif;font-size:24px}
.support{left:0;top:2561px;width:1200px;height:433px;overflow:hidden;background:#d42a23}
.footer{left:0;top:3519px;width:1200px;height:444px;background:var(--dark);color:#ddd}
.footer h6{position:absolute;top:60px;font-family:'Rubik',sans-serif;font-weight:500;font-size:20px;color:#fff}
.footer ul{position:absolute;top:102px;list-style:none;font-size:13.5px;line-height:27.3px;color:#d8d8d8}
.footer li::before{content:"›";margin-right:8px}
.contact-row{position:absolute;left:132px;display:flex;gap:12px;font-size:15.5px;line-height:23px;color:#e6e6e6}
</style>
</head>
<body>

<div class="abs alert-bar">Lorem Ipsum is simply dummy text of the printing and typesetting industry. Lorem Ipsum has been the industry's standard dummy text ever since...</div>

<header>
  <div class="abs brand" style="left:132px;top:48px">
    <div class="dot"></div>
    <span>AGW<br>FOUNDATION</span>
  </div>
  <div class="abs util" style="left:634px">
    <svg width="16" height="18" viewBox="0 0 16 18" fill="none" stroke="#e30613" stroke-width="1.6"><circle cx="8" cy="5" r="4"/><path d="M1 17c0-4 3-6 7-6s7 2 7 6"/></svg>MEMBERSHIP
  </div>
  <div class="abs util" style="left:784px">
    <svg width="18" height="18" viewBox="0 0 18 18" fill="none" stroke="#e30613" stroke-width="1.6"><circle cx="9" cy="9" r="7.5"/><path d="M5 9h7M9 6l3 3-3 3"/></svg>LOGIN
  </div>
  <div class="abs donate-btn">DONATE</div>
</header>

<nav class="abs main-nav">
  <a style="left:131px">GET HELP</a>
  <a style="left:251px">TAKE ACTION ⌵</a>
  <a style="left:403px">NEWS &amp; EVENTS ⌵</a>
  <a style="left:578px">SUPPORT ⌵</a>
  <a style="left:698px">OUR WORK ⌵</a>
  <a style="left:834px">ABOUT US ⌵</a>
  <a style="left:962px">CONTACT US</a>
</nav>

<section class="abs hero" role="img" aria-label="Sunlit farm field with rows of green crops under a blue sky"></section>
<div class="abs hero-welcome">Welcome To AGW Foundation</div>
<h1 class="abs head hero-title">Join The Peasant Movement</h1>
<div class="abs watch">
  <div class="play"><svg width="18" height="20" viewBox="0 0 18 20"><path d="M2 1l15 9-15 9z" fill="#fff"/></svg></div>
  WATCH THE OVERVIEW
</div>

<form class="abs signup">
  <h3>STAY INFORMED</h3>
  <div class="field" style="top:121px">Name*</div>
  <div class="field" style="top:180px">Email *</div>
  <div class="field" style="top:240px">Zip/Postal Code *</div>
  <div class="join">Join Now</div>
</form>

<section>
  <h2 class="abs head about-title">ABOUT<br>AGW FOUNDATION</h2>
  <p class="abs body-copy" style="left:131px;top:987px;width:430px">Lorem Ipsum is simply dummy text of the printing and typesetting industry. Lorem Ipsum has been industry's standard dummy text ever since the</p>
  <p class="abs body-copy" style="left:131px;top:1077px;width:430px">1500s, when an unknown printer took a galley of type and scrambled Lorem Ipsum is simply dummy text of the printing and typesetting industry.</p>
  <div class="abs outline-btn" style="left:131px;top:1182px;width:167px;height:49px;line-height:45px;font-size:16px">LEARN MORE</div>
  <div class="abs frame-b" style="left:637px;top:875px;width:442px;height:393px"></div>
  <div class="abs frame-a" style="left:617px;top:863px;width:452px;height:394px"></div>
  <div class="abs photo" style="left:628px;top:872px;width:440px;height:385px" role="img" aria-label="Group of volunteers outdoors raising joined hands together"></div>
</section>

<section class="abs events">
  <h2 class="abs head section-title" style="top:55px;color:#fff">UPCOMING EVENT</h2>
  <div class="arrow" style="left:128px"><svg width="12" height="16"><path d="M9 2L3 8l6 6" stroke="#fff" stroke-width="2" fill="none"/></svg></div>
  <div class="arrow" style="left:1031px"><svg width="12" height="16"><path d="M3 2l6 6-6 6" stroke="#fff" stroke-width="2" fill="none"/></svg></div>
  <article class="event-card" style="left:192px">
    <div class="img" style="background:linear-gradient(135deg,#2e4a6b,#8ea2b8 60%,#d9dde2)" role="img" aria-label="Business people applauding at a meeting table"></div>
    <h4>Lorem Ipsum is simply dummy text of the printing and typesetting</h4>
    <p>Lorem Ipsum is simply dummy text of the printing and typesetting industry. Lorem Ipsum has been</p>
    <div class="event-meta" style="left:24px;color:var(--teal)"><svg width="16" height="16" fill="none" stroke="#0a979d" stroke-width="1.5"><rect x="1" y="3" width="14" height="12"/><path d="M1 7h14M5 1v4M11 1v4"/></svg>Oct 8th, 2020</div>
    <div class="event-meta" style="left:254px;color:var(--red)"><svg width="13" height="17" fill="none" stroke="#e30613" stroke-width="1.5"><path d="M6.5 16s-5-6-5-9.5a5 5 0 0110 0c0 3.5-5 9.5-5 9.5z"/><circle cx="6.5" cy="6.5" r="2"/></svg>Place Name</div>
  </article>
  <article class="event-card" style="left:612px">
    <div class="img" style="background:linear-gradient(135deg,#5a6f7c,#a5b0b5 55%,#6b5c4e)" role="img" aria-label="Young group of students standing together"></div>
    <h4>Lorem Ipsum is simply dummy text of the printing and typesetting</h4>
    <p>Lorem Ipsum is simply dummy text of the printing and typesetting industry. Lorem Ipsum has been</p>
    <div class="event-meta" style="left:24px;color:var(--teal)"><svg width="16" height="16" fill="none" stroke="#0a979d" stroke-width="1.5"><rect x="1" y="3" width="14" height="12"/><path d="M1 7h14M5 1v4M11 1v4"/></svg>Oct 8th, 2020</div>
    <div class="event-meta" style="left:254px;color:var(--red)"><svg width="13" height="17" fill="none" stroke="#e30613" stroke-width="1.5"><path d="M6.5 16s-5-6-5-9.5a5 5 0 0110 0c0 3.5-5 9.5-5 9.5z"/><circle cx="6.5" cy="6.5" r="2"/></svg>Place Name</div>
  </article>
</section>

<section>
  <h2 class="abs head section-title" style="top:2028px">LATEST NEWS</h2>
  <article class="news-card" style="left:140px">
    <div class="img" style="background:linear-gradient(135deg,#c9c3b8,#8c8f96 60%,#5d6f86)" role="img" aria-label="Hands reading a newspaper"></div>
    <div class="date-badge"><small>JAN<br>2020</small><b>18</b></div>
    <h5>INDUSTRY'S STANDARD DUMMY TEXT EVER</h5>
    <p>Lorem Ipsum is simply dummy text of the printing &amp; typesetting industry. Lorem Ipsum</p>
    <div class="outline-btn">LEARN MORE</div>
  </article>
  <article class="news-card" style="left:457px">
    <div class="img" style="background:linear-gradient(135deg,#9fb86a,#d8d2a8 55%,#6f8f3a)" role="img" aria-label="Mother and child sitting in a sunny park"></div>
    <div class="date-badge"><small>JAN<br>2020</small><b>18</b></div>
    <h5>INDUSTRY'S STANDARD DUMMY TEXT EVER</h5>
    <p>Lorem Ipsum is simply dummy text of the printing &amp; typesetting industry. Lorem Ipsum</p>
    <div class="outline-btn">LEARN MORE</div>
  </article>
  <article class="news-card" style="left:774px">
    <div class="img" style="background:linear-gradient(135deg,#7d8a96,#4b5b75 55%,#a5aeb6)" role="img" aria-label="Group of people holding hands in a row"></div>
    <div class="date-badge"><small>JAN<br>2020</small><b>18</b></div>
    <h5>INDUSTRY'S STANDARD DUMMY TEXT EVER</h5>
    <p>Lorem Ipsum is simply dummy text of the printing &amp; typesetting industry. Lorem Ipsum</p>
    <div class="outline-btn">LEARN MORE</div>
  </article>
</section>

<section class="abs support" role="img" aria-label="Crowd of supporters celebrating together, tinted red and teal">
  <svg class="abs" style="left:0;top:0" width="1200" height="433"><circle cx="1115" cy="230" r="480" fill="#17979b"/></svg>
  <h2 class="abs" style="left:174px;top:120px;font-family:'Rubik',sans-serif;font-weight:700;font-size:40px;color:#fff">SUPPORT OUR WORK</h2>
  <p class="abs" style="left:174px;top:185px;width:420px;font-size:16px;line-height:23px;color:#fff">Lorem Ipsum is simply dummy text of the printing &amp; typesetting industry. Lorem Ipsum</p>
  <div class="abs" style="left:174px;top:250px;width:193px;height:48px;border:2px solid #fff;border-radius:25px;color:#fff;font-family:'Rubik',sans-serif;font-weight:500;font-size:16px;text-align:center;line-height:44px">DONATE NOW</div>
  <div class="abs" style="left:805px;top:116px;width:200px;height:200px;border-radius:50%;background:#fff;display:flex;align-items:center;justify-content:center;font-family:'Rubik',sans-serif;font-weight:700;font-size:30px;color:var(--ink)">AGW</div>
</section>

<section>
  <div class="abs frame-b" style="left:136px;top:3075px;width:434px;height:370px"></div>
  <div class="abs frame-a" style="left:126px;top:3063px;width:434px;height:369px"></div>
  <div class="abs" style="left:135px;top:3072px;width:425px;height:360px;background:linear-gradient(135deg,#b7a987,#6e7f96 55%,#c9c2b4)" role="img" aria-label="Smiling older couple looking at a laptop together"></div>
  <h2 class="abs head" style="left:611px;top:3094px;font-size:40px">SHARE YOUR STORY</h2>
  <p class="abs body-copy" style="left:611px;top:3155px;width:460px">Lorem Ipsum is simply dummy text of the printing and typesetting industry. Lorem Ipsum has been</p>
  <p class="abs body-copy" style="left:611px;top:3220px;width:460px">industry's standard dummy text ever since the 1500s, when an unknown printer took a galley of type and scrambled Lorem Ipsum is simply dummy text of the printing and typesetting industry.</p>
  <div class="abs outline-btn" style="left:611px;top:3358px;width:168px;height:48px;line-height:44px;font-size:16px">LEARN MORE</div>
</section>

<footer class="abs footer">
  <div class="abs" style="left:132px;top:53px;width:94px;height:94px;border-radius:50%;background:var(--red);color:#fff;font-family:'Rubik',sans-serif;font-weight:700;font-size:22px;display:flex;align-items:center;justify-content:center">AGW</div>
  <div class="contact-row" style="top:165px"><svg width="14" height="18" fill="none" stroke="#bbb" stroke-width="1.5"><path d="M7 17s-6-6-6-10a6 6 0 0112 0c0 4-6 10-6 10z"/><circle cx="7" cy="7" r="2"/></svg><span>#123 Address, Street 25<br>Dummy Address</span></div>
  <div class="abs" style="left:132px;top:223px;width:236px;height:1px;background:#555"></div>
  <div class="contact-row" style="top:236px"><svg width="16" height="16" fill="none" stroke="#bbb" stroke-width="1.5"><path d="M3 1h3l1.5 4-2 1.5a9 9 0 004 4l1.5-2 4 1.5v3a2 2 0 01-2 2A14 14 0 011 3a2 2 0 012-2z"/></svg>+888 888 8888</div>
  <div class="abs" style="left:132px;top:269px;width:236px;height:1px;background:#555"></div>
  <div class="contact-row" style="top:282px"><svg width="16" height="14" fill="none" stroke="#bbb" stroke-width="1.5"><rect x="1" y="1" width="14" height="11"/><path d="M1 1l7 6 7-6"/></svg>info@company.org</div>

  <h6 style="left:454px">COMPANY</h6>
  <ul style="left:454px"><li>Get Help</li><li>Take Action</li><li>News &amp; Events</li><li>Support</li><li>Our Work</li><li>About Us</li><li>Mission</li><li>Mesa Directiva</li></ul>
  <h6 style="left:638px">QUICK LINKS</h6>
  <ul style="left:638px;width:220px"><li>Brontalvo Network</li><li>Ciudadania</li><li>Peticiones Familiares</li><li>Sobrevivientes De Crimenes</li><li>Revision De Antecedentes</li><li>Accion Dieerida</li><li style="line-height:22px;padding-top:3px">Programa De Colegios<br>&nbsp;&nbsp;&nbsp;Comunidarios</li></ul>
  <h6 style="left:878px">QUICK LINKS</h6>
  <ul style="left:878px"><li>Para La Causa</li><li>Membrecia</li><li>Donacion Para La Causa</li><li>Servicio Voluntario</li><li>Oportunidades De Trabajo</li><li>Membrecia</li><li>Servicio Voluntario</li><li>Oportunidades De Trabajo</li></ul>

  <div class="abs" style="left:132px;top:358px;width:936px;height:1px;background:#4a4748"></div>
  <div class="abs" style="left:132px;top:389px;font-size:13px;color:#999">© 2020 AGW Foundation. All Rights are Reserved.</div>
  <svg class="abs" style="left:926px;top:382px" width="144" height="34" fill="none" stroke="#0a979d" stroke-width="2">
    <circle cx="17" cy="17" r="14"/><circle cx="53" cy="17" r="14"/><circle cx="89" cy="17" r="14"/><circle cx="125" cy="17" r="14"/>
  </svg>
</footer>

</body>
</html>
```